Shoes, Handbags and Accessories

The main business of the company are shoes and then handbags, jewellery and scarves to accessorize.

The design I am looking for is a "shabby chic" design, cursive font, perhaps with a vintage country feel to it.

Target Market(s)

Age group are more for the 25+, but more so 35+ ladies.

Industry/Entity Type

Business

Contact Information for Business Card

Lantern Row Boutique & Accessories
Marcia Pellbrook - P.O. Box 482, Yarrabin W.A. 6391
Ph: (08) 97213356 fax: (08) 97213374 Mobile: 0419382716
Email:lanternrow@quillnet.com.au
Web: www.lanternrowboutique.com.au
Like us on facebook (facebook logo)

Requirements
Must have
• As already described. A "faded" picture background is also another feature I like, but I don't want to create a cluttered look about the business card.
Nice to have
• Classy, stylish and comfortable shoes.

```html
<!DOCTYPE html>
<html lang="en">
<head>
<meta charset="utf-8">
<title>Lantern Row Boutique &amp; Accessories — Business Card</title>
<link rel="stylesheet" href="https://fonts.googleapis.com/css2?family=Dancing+Script:wght@400;500&display=swap">
<style>
  :root {
    --backdrop-light: #ffffff;
    --backdrop-dark: #dcdddf;
    --plum-light: #67308f;
    --plum-dark: #3f0c5a;
    --lilac: #c5b3d9;
    --lilac-deep: #b09ccb;
    --ornament-pale: #c9b3e0;
    --title-mauve: #6e4f8f;
    --ink-purple: #5a3d80;
    --band-purple: #662d91;
    --white: #ffffff;
  }
  * { margin: 0; padding: 0; box-sizing: border-box; }
  html, body { width: 1200px; height: 1000px; overflow: hidden; }
  body {
    position: relative;
    background: radial-gradient(ellipse at 50% 48%, var(--backdrop-light) 0%, #f3f3f4 35%, var(--backdrop-dark) 100%);
    font-family: "Dancing Script", cursive;
  }
  .card {
    position: absolute;
    left: 257px;
    width: 640px;
    height: 331px;
    border-radius: 10px;
    overflow: hidden;
  }
  .card--front {
    top: 107px;
    background: linear-gradient(90deg, var(--plum-light) 0%, #552280 45%, var(--plum-dark) 100%);
    color: var(--white);
  }
  .card--back {
    top: 527px;
    background: var(--lilac);
    color: var(--ink-purple);
  }
  .centered { position: absolute; left: 0; width: 100%; text-align: center; white-space: nowrap; }
  .front-title { top: 30px; left: 40px; width: 536px; font-size: 54px; font-weight: 400; }
  .front-amp { top: 120px; left: 0; width: 616px; font-size: 24px; }
  .front-owner { top: 175px; left: 0; width: 616px; font-size: 33px; }
  .ornament {
    position: absolute;
    background: var(--ornament-pale);
  }
  .ornament--corner-left { left: 10px; top: 10px; width: 62px; height: 74px; border-radius: 40% 60% 50% 50%; opacity: 0.85; }
  .ornament--corner-right { right: 10px; top: 10px; width: 62px; height: 74px; border-radius: 60% 40% 50% 50%; opacity: 0.85; }
  .ornament--scroll { left: 40px; top: 262px; width: 560px; height: 56px; border-radius: 50%; opacity: 0.35; }
  .back-swoosh { position: absolute; left: 0; top: 0; }
  .back-title { top: 18px; left: 90px; width: 434px; font-size: 42px; color: var(--title-mauve); }
  .back-amp { top: 72px; left: 0; width: 604px; font-size: 18px; }
  .back-owner { top: 104px; left: 120px; width: 434px; font-size: 22px; }
  .contact { position: absolute; left: 26px; top: 184px; line-height: 1; }
  .contact p { white-space: nowrap; }
  .contact .address { font-size: 21px; margin-bottom: 8px; }
  .contact .phone { font-size: 21px; margin-bottom: 8px; }
  .contact .mobile { font-size: 16px; }
  .ornament--knot {
    position: absolute; left: 490px; top: 63px; width: 104px; height: 195px;
    background: var(--band-purple);
    clip-path: polygon(50% 0, 100% 50%, 50% 100%, 0 50%);
    opacity: 0.85;
  }
  .web-band { position: absolute; left: 0; bottom: 0; }
  .web-address {
    position: absolute; right: 80px; bottom: 4px; font-size: 15px; color: var(--white); white-space: nowrap;
  }
</style>
</head>
<body>

<section class="card card--front" aria-label="Business card front">
  <div class="ornament ornament--corner-left" role="img" aria-label="Decorative corner flourish"></div>
  <div class="ornament ornament--corner-right" role="img" aria-label="Decorative corner flourish"></div>
  <h1 class="centered front-title">Lantern Row Boutique</h1>
  <p class="centered front-amp">&amp;</p>
  <p class="centered front-owner">Accessories Marcia Pellbrook</p>
  <div class="ornament ornament--scroll" role="img" aria-label="Decorative scroll flourish"></div>
</section>

<section class="card card--back" aria-label="Business card back">
  <svg class="back-swoosh" width="200" height="331" viewBox="0 0 200 331" aria-hidden="true">
    <path d="M0 0 H110 C70 60 55 150 110 240 C140 290 150 315 155 331 H0 Z" fill="var(--lilac-deep)" opacity="0.55"/>
    <path d="M40 0 C20 90 30 200 90 331 H60 C10 220 5 100 25 0 Z" fill="var(--lilac-deep)" opacity="0.6"/>
    <path d="M0 120 C60 150 110 200 150 331" fill="none" stroke="var(--white)" stroke-opacity="0.35" stroke-width="1"/>
  </svg>
  <h2 class="centered back-title">Lantern Row Boutique</h2>
  <p class="centered back-amp">&amp;</p>
  <p class="centered back-owner">Accessories Marcia Pellbrook</p>
  <div class="contact">
    <p class="address">P.O. Box 482, Yarrabin W.A. 6391</p>
    <p class="phone">Ph: (08) 97213356</p>
    <p class="mobile">Mobile: 0419382716</p>
  </div>
  <div class="ornament--knot" role="img" aria-label="Decorative knot ornament"></div>
  <svg class="web-band" width="640" height="26" viewBox="0 0 640 26" aria-hidden="true">
    <polygon points="293,26 320,0 640,0 640,26" fill="var(--band-purple)"/>
  </svg>
  <p class="web-address">www.lanternrowboutique.com.au</p>
</section>

</body>
</html>
```